Business Card design for an International Import Export House

We need a Business Card design for our import export business. We trade in Minerals, Metals, Rice, Sugar, Steel etc.. The design should be minimalistic. It may or may not contain the physical address. In case you want to include the physical address - 418 Verandah Heights, Marlow Sector 9, Ardenpur, Kestrel State, India, 410278.

Target Market(s)

Steel Mills or Steel Plants, Factories, Mining businesses, Industrial houses, Government Agencies

Industry/Entity Type

Importer

Contact Information for Business Card

Business Name - Tessan Overseas

Font styles to use
Other font styles liked:
• montserrat

Requirements
Must have
• Ravi Kandola - President
• www.tessanoverseas.com
• ravi@tessanoverseas.com
• +91-987-654-3217
Nice to have
• worldwide suppliers of ores

```html
<!DOCTYPE html>
<html lang="en">
<head>
<meta charset="utf-8">
<title>Tessan Overseas – Business Card</title>
<link rel="stylesheet" href="https://fonts.googleapis.com/css2?family=Montserrat:wght@400;500;600;700&display=swap">
<style>
  :root {
    --backdrop: #d4d9d7;
    --paper: #f2f2f0;
    --paper-edge: #e2e3e1;
    --brand-teal: #2f7493;
    --ink: #1f2224;
    --ink-soft: #3a3d40;
    --rule: #4a4d50;
  }
  * { box-sizing: border-box; margin: 0; padding: 0; }
  html, body {
    width: 1200px;
    height: 1000px;
    overflow: hidden;
    background: var(--backdrop);
    font-family: "Montserrat", sans-serif;
  }
  .stage {
    position: relative;
    width: 1200px;
    height: 1000px;
  }
  .card {
    position: absolute;
    top: 350px;
    width: 520px;
    height: 300px;
    background: var(--paper);
    border: 1px solid var(--paper-edge);
    box-shadow: 0 10px 24px rgba(60, 70, 68, 0.18);
  }
  .card--contact { left: 50px; }
  .card--front { left: 630px; }

  /* Contact side */
  .contact-brand {
    position: absolute;
    left: 44px;
    top: 36px;
    display: flex;
    align-items: center;
    gap: 8px;
  }
  .brand-dot {
    width: 14px;
    height: 14px;
    border-radius: 50%;
    background: var(--brand-teal);
  }
  .brand-name {
    font-weight: 700;
    color: var(--brand-teal);
    letter-spacing: 0.02em;
    text-transform: uppercase;
  }
  .contact-brand .brand-name { font-size: 14px; }
  .holder {
    position: absolute;
    left: 44px;
    top: 86px;
  }
  .holder-name {
    font-size: 22px;
    font-weight: 500;
    color: var(--ink);
    letter-spacing: 0.04em;
    text-transform: uppercase;
  }
  .holder-role {
    margin-top: 4px;
    font-size: 11px;
    font-weight: 500;
    color: var(--ink-soft);
    letter-spacing: 0.14em;
    text-transform: uppercase;
  }
  .divider {
    position: absolute;
    left: 280px;
    top: 110px;
    width: 1px;
    height: 72px;
    background: var(--rule);
  }
  .details {
    position: absolute;
    left: 300px;
    top: 112px;
    width: 200px;
    font-size: 12px;
    line-height: 1.45;
    color: var(--ink);
  }
  .details address { font-style: normal; margin-bottom: 8px; }
  .details p { margin-bottom: 2px; }
  .website {
    position: absolute;
    left: 44px;
    bottom: 40px;
    font-size: 13px;
    font-weight: 500;
    color: var(--ink);
  }

  /* Front side */
  .front-lockup {
    position: absolute;
    left: 0;
    right: 0;
    top: 98px;
    display: flex;
    flex-direction: column;
    align-items: center;
  }
  .front-brand {
    display: flex;
    align-items: center;
    gap: 12px;
  }
  .front-brand .brand-dot { width: 26px; height: 26px; }
  .front-brand .brand-name { font-size: 28px; }
  .front-rule {
    width: 320px;
    height: 1px;
    margin-top: 12px;
    background: var(--rule);
  }
  .tagline {
    margin-top: 10px;
    font-size: 11px;
    font-weight: 600;
    letter-spacing: 0.22em;
    color: var(--ink-soft);
    text-transform: uppercase;
  }
</style>
</head>
<body>
<main class="stage">
  <section class="card card--contact">
    <div class="contact-brand">
      <span class="brand-dot"></span>
      <span class="brand-name">Tessan Overseas</span>
    </div>
    <div class="holder">
      <h1 class="holder-name">Ravi Kandola</h1>
      <p class="holder-role">President</p>
    </div>
    <span class="divider"></span>
    <div class="details">
      <address>418 Verandah Heights, Marlow Sector 9, Ardenpur, Kestrel State, India, 410278</address>
      <p>ravi@tessanoverseas.com</p>
      <p>+91-987-654-3217</p>
    </div>
    <p class="website">www.tessanoverseas.com</p>
  </section>

  <section class="card card--front">
    <div class="front-lockup">
      <div class="front-brand">
        <span class="brand-dot"></span>
        <span class="brand-name">Tessan Overseas</span>
      </div>
      <span class="front-rule"></span>
      <p class="tagline">Worldwide Suppliers of Ores</p>
    </div>
  </section>
</main>
</body>
</html>
```